email direct marketing for travel agent

we need a single page for direct mail to promote our travel agent in greece

New Breifing 
Please not to emphasized on a shopping keywords with priority are
1. live the myth
2. weekend in Athens 
3. Summer all the year
4. City break with 3 islands tour
5. Shopping 
The keywords are not necessary to include in the poster The whole message are go to Athens for a long weekend 

Target Market(s)

Affluent travellers

Industry/Entity Type

Marketing

Font styles to use
Sans Serif

Colors
33a6d7
85cae6
0455a3
3176b5
eb1f27

Requirements
Must have
• leisure history relax comfortable luxury shopping

```html
<!DOCTYPE html>
<html lang="en">
<head>
<meta charset="utf-8">
<title>Helios Escapes – A Weekend in Athens</title>
<link rel="stylesheet" href="https://fonts.googleapis.com/css2?family=Archivo+Black&family=Roboto+Condensed:wght@300;400;700;900&display=swap">
<style>
  :root {
    --sky-blue: #33a6d7;
    --pale-blue: #85cae6;
    --deep-blue: #0455a3;
    --mid-blue: #3176b5;
    --offer-red: #eb1f27;
    --offer-red-dark: #b8141b;
    --white: #ffffff;
    --ink-shadow: #3a3f4a;
  }
  html, body {
    margin: 0;
    padding: 0;
    width: 849px;
    height: 1200px;
    overflow: hidden;
    background: var(--white);
  }
  .poster {
    position: relative;
    width: 849px;
    height: 1200px;
    overflow: hidden;
    background: var(--white);
    font-family: "Roboto Condensed", sans-serif;
  }
  .poster__art {
    position: absolute;
    inset: 0;
    width: 849px;
    height: 1200px;
  }

  /* Offer tag */
  .offer-tag {
    position: absolute;
    left: 506px;
    top: 52px;
    width: 330px;
    height: 130px;
    transform: rotate(-15deg);
    transform-origin: center;
    background: linear-gradient(180deg, var(--offer-red) 0%, var(--offer-red-dark) 100%);
    clip-path: polygon(0 0, 88% 0, 100% 50%, 88% 100%, 0 100%);
    color: var(--white);
    text-align: center;
    font-family: "Archivo Black", sans-serif;
    text-transform: uppercase;
    line-height: 1;
  }
  .offer-tag__stitch {
    position: absolute;
    inset: 8px 36px 8px 8px;
    border: 2px dashed rgba(255,255,255,0.85);
  }
  .offer-tag__hole {
    position: absolute;
    right: 14px;
    top: 56px;
    width: 14px;
    height: 14px;
    border-radius: 50%;
    background: #dfe6ee;
    border: 2px solid #7d848d;
  }
  .offer-tag__text {
    position: absolute;
    left: 10px;
    right: 42px;
    top: 18px;
    margin: 0;
  }
  .offer-tag__title { display: block; font-size: 28px; }
  .offer-tag__detail { display: block; font-size: 17px; margin-top: 5px; }
  .offer-tag__price { display: block; font-size: 38px; margin-top: 4px; }

  /* Headline */
  .headline {
    position: absolute;
    right: 84px;
    top: 290px;
    margin: 0;
    text-align: right;
    font-family: "Roboto Condensed", sans-serif;
    font-weight: 900;
    font-size: 86px;
    line-height: 86px;
    color: var(--white);
    text-transform: uppercase;
    text-shadow: 2px 2px 0 var(--ink-shadow), 4px 4px 0 var(--ink-shadow), 6px 6px 6px rgba(0,0,0,0.3);
  }

  /* Tagline */
  .tagline {
    position: absolute;
    left: 84px;
    top: 850px;
    margin: 0;
    color: var(--deep-blue);
    text-transform: uppercase;
    line-height: 1;
  }
  .tagline__line {
    display: block;
    font-weight: 300;
    font-size: 62px;
    letter-spacing: -2px;
    margin-bottom: 3px;
  }
  .tagline__strong { font-weight: 900; letter-spacing: -1px; }
  .tagline__sub {
    display: block;
    font-weight: 300;
    font-size: 29px;
    margin-top: 6px;
  }

  /* Brand block */
  .brand {
    position: absolute;
    left: 542px;
    top: 1020px;
    width: 240px;
    text-align: center;
  }
  .brand__name {
    display: inline-flex;
    align-items: center;
    gap: 10px;
    font-weight: 700;
    font-size: 29px;
    color: var(--deep-blue);
  }
  .brand__dot {
    width: 18px;
    height: 18px;
    border-radius: 50%;
    background: var(--sky-blue);
  }
  .brand__social {
    display: flex;
    align-items: center;
    justify-content: center;
    gap: 7px;
    margin-top: 12px;
    font-weight: 400;
    font-size: 18px;
    color: var(--deep-blue);
  }
  .brand__social-mark {
    width: 14px;
    height: 14px;
    background: var(--pale-blue);
  }
</style>
</head>
<body>
<main class="poster">
  <svg class="poster__art" viewBox="0 0 849 1200">
    <defs>
      <linearGradient id="sky" x1="0" y1="0" x2="0.3" y2="1">
        <stop offset="0" stop-color="#2c5aa6"/>
        <stop offset="0.35" stop-color="#4e80c2"/>
        <stop offset="0.7" stop-color="#9fbcdc"/>
        <stop offset="1" stop-color="#dcc4b8"/>
      </linearGradient>
      <radialGradient id="marble" cx="0.28" cy="0.58" r="0.5">
        <stop offset="0" stop-color="#e6e2da"/>
        <stop offset="0.55" stop-color="#d3cec5" stop-opacity="0.9"/>
        <stop offset="1" stop-color="#d3cec5" stop-opacity="0"/>
      </radialGradient>
      <linearGradient id="city" x1="0" y1="0" x2="0" y2="1">
        <stop offset="0" stop-color="#2a3d8e"/>
        <stop offset="0.6" stop-color="#34407a"/>
        <stop offset="1" stop-color="#4a4536"/>
      </linearGradient>
      <radialGradient id="glow" cx="0.5" cy="0.6" r="0.4">
        <stop offset="0" stop-color="#e6c27a" stop-opacity="0.85"/>
        <stop offset="0.5" stop-color="#b38b4a" stop-opacity="0.45"/>
        <stop offset="1" stop-color="#b38b4a" stop-opacity="0"/>
      </radialGradient>
    </defs>

    <g role="img" aria-label="Photo: marble statue of a seated bearded philosopher in thought against a bright blue sky with clouds">
      <polygon points="0,0 849,0 849,640 0,585" fill="url(#sky)"/>
      <polygon points="0,0 849,0 849,640 0,585" fill="url(#marble)"/>
    </g>

    <polygon class="band band--top" points="0,583 849,638 849,652 0,597" fill="var(--sky-blue)"/>

    <g role="img" aria-label="Photo: the Acropolis and Parthenon illuminated at dusk above the lights of Athens">
      <polygon points="0,597 849,652 849,848 0,735" fill="url(#city)"/>
      <polygon points="0,597 849,652 849,848 0,735" fill="url(#glow)"/>
    </g>

    <polygon class="band band--bottom" points="0,735 849,848 849,868 0,751" fill="var(--sky-blue)"/>
  </svg>

  <div class="offer-tag">
    <span class="offer-tag__stitch"></span>
    <span class="offer-tag__hole"></span>
    <p class="offer-tag__text">
      <span class="offer-tag__title">Special Offer</span>
      <span class="offer-tag__detail">A Weekend in Athens</span>
      <span class="offer-tag__price">Only £199</span>
    </p>
  </div>

  <h1 class="headline">Deciding<br>where<br>to go?</h1>

  <p class="tagline">
    <span class="tagline__line">Experience.</span>
    <span class="tagline__line">Relax.<span class="tagline__strong">Enjoy</span></span>
    <span class="tagline__line">Visit <span class="tagline__strong">Greece.</span></span>
    <span class="tagline__sub">For your perfect holiday</span>
  </p>

  <div class="brand">
    <div class="brand__name"><span class="brand__dot"></span>Helios Escapes</div>
    <div class="brand__social"><span class="brand__social-mark"></span>social.example/HeliosEscapes</div>
  </div>
</main>
</body>
</html>
```